TRESSLY FACEBOOK DESIGN

I need new design for facebook https://www.facebook.com/tresslyitalia.
Our Businnes is Hair care , hair replacement , hair transplant . hair regrowth . i NEED MEDICAL AND PROFESSIONAL DESIGN. I NEED ALSO RESPONSIVE DESIGN

Target Market(s)

Consumers

Industry/Entity Type

MEDICAL AND COSMETICS

Colors
0054AA
0677BA
7BADD7
CADEEF
E8F1F8

Requirements
Must have
• MEDICAL
Nice to have
• RESPONSIVE DESIGN

```html
<!DOCTYPE html>
<html lang="it">
<head>
<meta charset="utf-8">
<title>Tressly – Facebook Covers</title>
<link rel="stylesheet" href="https://fonts.googleapis.com/css2?family=Mulish:wght@400;600;700&display=swap">
<style>
  :root {
    --blue-deep: #0054AA;
    --blue-mid: #0677BA;
    --blue-soft: #7BADD7;
    --blue-pale: #CADEEF;
    --blue-mist: #E8F1F8;
    --ink: #1d1d1f;
    --page: #dcdcdc;
    --white: #ffffff;
  }
  * { box-sizing: border-box; margin: 0; padding: 0; }
  html, body { width: 1193px; height: 1200px; overflow: hidden; }
  body { background: var(--page); font-family: "Mulish", Arial, sans-serif; color: var(--ink); position: relative; }

  .cover {
    position: absolute; left: 55px; width: 1095px; height: 535px;
    background: var(--white); overflow: hidden;
    box-shadow: 0 2px 8px rgba(0,0,0,.18);
  }
  .cover--men { top: 48px; }
  .cover--women { top: 617px; }
  .cover__shapes { position: absolute; inset: 0; width: 100%; height: 100%; }

  .photo { position: absolute; }
  .photo--man {
    left: 690px; top: 0; width: 405px; height: 535px;
    background: linear-gradient(180deg, #6b4a35 0%, #4a3327 30%, #e8e6e2 55%, #3c2b24 100%);
  }
  .photo--bottle-top {
    left: 503px; top: 60px; width: 105px; height: 345px; border-radius: 36px 36px 14px 14px;
    background: linear-gradient(90deg, #d9dde2, #ffffff 45%, #cfd4da);
  }
  .photo--woman {
    left: 0; top: 0; width: 520px; height: 535px;
    background: linear-gradient(120deg, #1c1614 0%, #5a3d30 40%, #c79a80 55%, #2a1e1a 100%);
  }
  .photo--bottle-bottom {
    left: 530px; top: 28px; width: 110px; height: 350px; border-radius: 36px 36px 14px 14px;
    background: linear-gradient(90deg, #d9dde2, #ffffff 45%, #cfd4da);
  }

  .brand { position: absolute; display: flex; flex-direction: column; }
  .brand__row { display: flex; align-items: center; gap: 12px; }
  .brand__mark { width: 30px; height: 30px; background: var(--blue-mid); border-radius: 50%; }
  .brand__name { font-weight: 700; font-size: 42px; color: var(--blue-deep); letter-spacing: 1px; line-height: 1; }
  .brand__tagline { font-weight: 600; font-size: 13px; color: var(--blue-deep); margin-top: 8px; letter-spacing: .3px; }
  .cover--men .brand { left: 22px; top: 32px; }
  .cover--women .brand { left: 742px; top: 48px; }
  .cover--women .brand__name { font-size: 52px; }
  .cover--women .brand__mark { width: 36px; height: 36px; }
  .cover--women .brand__tagline { font-size: 16px; }

  .headline { position: absolute; font-weight: 600; font-size: 42px; color: var(--blue-deep); letter-spacing: .5px; white-space: nowrap; }
  .headline__accent { color: var(--blue-mid); }
  .cover--men .headline { left: 12px; top: 192px; }
  .cover--women .headline { left: 668px; top: 222px; }

  .intro { position: absolute; font-size: 23px; line-height: 1.5; color: var(--ink); white-space: nowrap; }
  .cover--men .intro { left: 12px; top: 252px; }
  .cover--women .intro { right: 46px; top: 288px; text-align: right; }

  .cta {
    position: absolute; width: 206px; height: 68px; border-radius: 10px;
    background: var(--blue-deep); color: var(--white);
    font-weight: 600; font-size: 23px; display: flex; align-items: center; justify-content: center;
    box-shadow: 0 4px 10px rgba(0,40,90,.35);
  }
  .cover--men .cta { left: 10px; top: 343px; }
  .cover--women .cta { left: 852px; top: 378px; }

  .call { position: absolute; display: flex; align-items: center; color: var(--blue-deep); }
  .call__icon { width: 36px; height: 36px; }
  .cover--men .call { left: 12px; top: 455px; gap: 10px; }
  .call__label { font-size: 22px; font-weight: 600; }
  .call__number { font-size: 29px; font-weight: 600; margin-left: 14px; }
  .cover--women .call { left: 550px; top: 410px; flex-direction: column; color: var(--white); width: 230px; }
  .cover--women .call__icon { width: 40px; height: 40px; }
  .cover--women .call__label { margin-top: 12px; font-weight: 400; }
  .cover--women .call__number { margin-left: 0; font-size: 28px; font-weight: 400; }
</style>
</head>
<body>

<section class="cover cover--men" aria-label="Tressly cover, men">
  <svg class="cover__shapes" viewBox="0 0 1095 535" preserveAspectRatio="none" aria-hidden="true">
    <polygon points="400,0 1095,0 1095,535 360,535 520,300" fill="var(--blue-deep)"/>
    <polygon points="400,0 445,0 620,240 600,260" fill="var(--blue-mid)"/>
    <polygon points="360,535 410,535 510,400 490,380" fill="var(--white)"/>
    <circle cx="555" cy="278" r="165" fill="var(--blue-pale)"/>
    <circle cx="555" cy="278" r="138" fill="var(--white)"/>
  </svg>
  <div class="photo photo--man" role="img" aria-label="Photo of a young man with styled hair in a brown jacket"></div>
  <div class="photo photo--bottle-top" role="img" aria-label="Product photo of a white shampoo bottle with pump"></div>

  <div class="brand">
    <div class="brand__row"><span class="brand__mark"></span><span class="brand__name">TRESSLY</span></div>
    <span class="brand__tagline">CURA E REINTEGRAZIONE DEI CAPELLI</span>
  </div>
  <h1 class="headline">TRESSLY <span class="headline__accent">ITALIA</span></h1>
  <p class="intro">Lorem ipsum dolor sit amet,<br>consectetur adipiscing elit, sed do</p>
  <div class="cta">SHOP NOW</div>
  <div class="call">
    <svg class="call__icon" viewBox="0 0 36 36" aria-hidden="true">
      <circle cx="18" cy="18" r="18" fill="var(--blue-deep)"/>
      <path d="M13 9c1 0 3 4 3 5s-2 2-2 3 3 5 5 5 2-2 3-2 5 2 5 3-2 4-4 4C16 27 9 20 9 13c0-2 3-4 4-4z" fill="var(--white)"/>
    </svg>
    <span class="call__label">CALL</span><span class="call__number">+39 800 123 456</span>
  </div>
</section>

<section class="cover cover--women" aria-label="Tressly cover, women">
  <svg class="cover__shapes" viewBox="0 0 1095 535" preserveAspectRatio="none" aria-hidden="true">
    <defs>
      <linearGradient id="waveFill" x1="0" y1="0" x2="1" y2="0">
        <stop offset="0" stop-color="var(--blue-mid)"/>
        <stop offset="1" stop-color="var(--blue-soft)"/>
      </linearGradient>
    </defs>
    <path d="M520,370 C650,330 760,420 880,420 C980,420 1040,500 1095,500 L1095,535 L520,535 Z" fill="url(#waveFill)"/>
  </svg>
  <div class="photo photo--woman" role="img" aria-label="Photo of a woman with long dark wavy hair"></div>
  <div class="photo photo--bottle-bottom" role="img" aria-label="Product photo of a white shampoo bottle with pump"></div>

  <div class="brand">
    <div class="brand__row"><span class="brand__mark"></span><span class="brand__name">TRESSLY</span></div>
    <span class="brand__tagline">CURA E REINTEGRAZIONE DEI CAPELLI</span>
  </div>
  <h2 class="headline">TRESSLY <span class="headline__accent">ITALIA</span></h2>
  <p class="intro">Lorem ipsum dolor sit amet,<br>consectetur adipiscing elit, sed do</p>
  <div class="cta">SHOP NOW</div>
  <div class="call">
    <svg class="call__icon" viewBox="0 0 36 36" aria-hidden="true">
      <circle cx="18" cy="18" r="18" fill="var(--white)"/>
      <path d="M13 9c1 0 3 4 3 5s-2 2-2 3 3 5 5 5 2-2 3-2 5 2 5 3-2 4-4 4C16 27 9 20 9 13c0-2 3-4 4-4z" fill="var(--blue-mid)"/>
    </svg>
    <span class="call__label">CALL</span>
    <span class="call__number">+39 800 123 456</span>
  </div>
</section>

</body>
</html>
```